Flyer Design

I'm looking for a new flyer design to help promote our landscape company, and some of our main service for the up and coming season. We're trying to position ourselves as a leader in our market, so obviously quality is important to us.

Our current promotion is 25% off the first month with signup of annual service.

Phone Number: (555) 213-0948
Website: verdlanex.com
Our tagline: "Your hands are full... Let us help"

The call to action: direct them to our website for a detailed list of services and to receive a free quote.

You're welcome to add your own wording and punctuation. If I like the design I will provide feedback accordingly.

I have attached a jpg of our logo to help with design colors. I will provide the vector file upon completion of this project.

Also, I've attached a few photos that I had on hand of our companies work that may help with the design. Obviously I don't want to use them all, but there are a couple just to help out. I'm not opposed to stock photos either.
Thanks

Target Market(s)

We market to high end customers, generally with home between $500k-$2mil, or household income over $200k. Quality and creativity are most important to us.

Industry/Entity Type

Landscape

Requirements
Must have
• Creativity, easy to read, modern style.

```html
<!DOCTYPE html>
<html lang="en">
<head>
<meta charset="UTF-8">
<title>Verdlane Lawn &amp; Landscape Flyer</title>
<link href="https://fonts.googleapis.com/css2?family=Oswald:wght@300;400;600&family=Open+Sans:wght@400;600&display=swap" rel="stylesheet">
<style>
  :root {
    --paper: #ffffff;
    --ink: #2b2b2b;
    --brand-orange: #d9572b;
    --brand-dark: #2a2a2a;
    --lawn-light: #7fa33a;
    --lawn-mid: #5f8a26;
    --lawn-dark: #476d19;
    --leaf-orange: #d9822b;
    --leaf-gold: #e8a63b;
    --garden-green: #4f7a34;
    --garden-sky: #9fbf86;
  }
  * { margin: 0; padding: 0; box-sizing: border-box; }
  html, body { width: 1200px; height: 924px; overflow: hidden; background: var(--paper); }
  .flyer { position: relative; width: 1200px; height: 924px; background: var(--paper); overflow: hidden; }

  .photo { position: absolute; }
  .photo-mower {
    left: 0; top: 0; width: 393px; height: 387px;
    background: linear-gradient(160deg, #a9c46b 0%, var(--lawn-mid) 45%, #3b3b3b 60%, #b3261e 75%, var(--lawn-light) 100%);
  }
  .photo-leaves {
    left: 412px; top: 0; width: 383px; height: 387px;
    background: radial-gradient(circle at 40% 40%, var(--leaf-gold), var(--leaf-orange) 55%, #9c4a1c 100%);
  }
  .photo-garden {
    left: 812px; top: 0; width: 388px; height: 387px;
    background: linear-gradient(180deg, #c9d9b0 0%, var(--garden-sky) 20%, var(--garden-green) 55%, #c94c6a 75%, #3f6a2c 100%);
  }
  .photo-lawn {
    left: 0; top: 405px; width: 1200px; height: 440px;
    background: linear-gradient(100deg, var(--lawn-dark) 0%, var(--lawn-light) 30%, var(--lawn-mid) 55%, var(--lawn-light) 80%, var(--lawn-dark) 100%);
  }

  .brand-badge {
    position: absolute; left: 442px; top: 278px; width: 316px; height: 182px;
    background: var(--paper); border-radius: 50%;
    box-shadow: 0 4px 10px rgba(0,0,0,0.35);
    display: flex; align-items: center; justify-content: center; gap: 12px;
  }
  .brand-dot { width: 22px; height: 22px; border-radius: 50%; background: var(--brand-orange); }
  .brand-name {
    font-family: 'Oswald', sans-serif; font-weight: 600; font-size: 44px;
    color: var(--brand-dark); letter-spacing: 1px; text-transform: uppercase;
  }

  .tagline {
    position: absolute; left: 0; top: 500px; width: 1200px; text-align: center;
    font-family: 'Oswald', sans-serif; font-weight: 300; font-size: 80px; line-height: 92px;
    color: var(--paper);
  }

  .promo {
    position: absolute; left: 0; top: 696px; width: 1200px; text-align: center;
    font-family: 'Oswald', sans-serif; font-weight: 400; font-size: 34px; line-height: 44px;
    color: var(--paper); letter-spacing: 1px;
  }
  .promo-highlight {
    display: inline-block; padding: 0 12px; margin-right: 6px;
    background: var(--brand-orange); color: var(--paper);
  }

  .call-to-action {
    position: absolute; left: 0; top: 748px; width: 1200px; text-align: center;
    font-family: 'Open Sans', sans-serif; font-weight: 600; font-size: 22px; line-height: 30px;
    color: var(--paper);
  }
  .phone-icon { width: 20px; height: 20px; vertical-align: -3px; margin: 0 6px 0 18px; }

  .bottom-curve { position: absolute; left: 0; top: 800px; width: 1200px; height: 124px; }

  .website {
    position: absolute; left: 0; top: 832px; width: 1200px; text-align: center;
    font-family: 'Open Sans', sans-serif; font-weight: 400; font-size: 58px;
    letter-spacing: 3px; color: var(--ink);
  }
</style>
</head>
<body>
  <main class="flyer">
    <div class="photo photo-mower" role="img" aria-label="Ride-on mower cutting a striped green lawn"></div>
    <div class="photo photo-leaves" role="img" aria-label="Pile of orange autumn leaves with a rake"></div>
    <div class="photo photo-garden" role="img" aria-label="Landscaped garden with a curving path and flower beds"></div>
    <div class="photo photo-lawn" role="img" aria-label="Freshly mowed striped lawn"></div>

    <div class="brand-badge">
      <span class="brand-dot"></span>
      <span class="brand-name">Verdlane</span>
    </div>

    <h1 class="tagline">Your hands are full...<br>Let us help</h1>

    <p class="promo"><span class="promo-highlight">25% OFF</span> your first month with annual service</p>

    <p class="call-to-action">
      Visit our website for a full list of services &amp; a free quote
      <svg class="phone-icon" viewBox="0 0 24 24" aria-hidden="true"><path fill="currentColor" d="M6.6 10.8a15.1 15.1 0 0 0 6.6 6.6l2.2-2.2a1 1 0 0 1 1-.25 11.4 11.4 0 0 0 3.6.57 1 1 0 0 1 1 1V20a1 1 0 0 1-1 1A17 17 0 0 1 3 4a1 1 0 0 1 1-1h3.5a1 1 0 0 1 1 1c0 1.25.2 2.45.57 3.6a1 1 0 0 1-.25 1z"/></svg>(555) 213-0948
    </p>

    <svg class="bottom-curve" viewBox="0 0 1200 124" preserveAspectRatio="none" aria-hidden="true">
      <path d="M0 36 Q600 -10 1200 36 L1200 124 L0 124 Z" fill="var(--paper)"/>
    </svg>

    <p class="website">verdlanex.com</p>
  </main>
</body>
</html>
```